Criação de Papelaria Profissional para Limpeza & Serviço para o lar
" Nossa empresa e familiar, buscamos fazer nosso trabalho com excelencia e qualidade visando o bem estar de nossos clientes. "

```html
<!DOCTYPE html>
<html lang="pt-BR">
<head>
<meta charset="UTF-8">
<title>Assinatura de e-mail – TidyNest Cleaning</title>
<link rel="stylesheet" href="https://fonts.googleapis.com/css2?family=Poppins:wght@300;400;500;600&display=swap">
<style>
  :root {
    --page-bg: #eef1f0;
    --card-bg: #ffffff;
    --mint: #5ccaa1;
    --mint-light: #8fe0c2;
    --mint-pale: #d8f4e9;
    --accent-orange: #c7813f;
    --contact-tan: #c9955e;
    --white: #ffffff;
  }
  * { margin: 0; padding: 0; box-sizing: border-box; }
  html, body {
    width: 1200px;
    height: 1200px;
    overflow: hidden;
    background: var(--page-bg);
    font-family: "Poppins", sans-serif;
  }
  .canvas {
    width: 1200px;
    height: 1200px;
    display: flex;
    align-items: center;
    justify-content: center;
  }
  .signature {
    position: relative;
    width: 1080px;
    height: 170px;
    background: linear-gradient(90deg, var(--card-bg) 0%, var(--card-bg) 56%, var(--mint-pale) 68%, var(--mint-light) 80%, var(--mint) 100%);
    box-shadow: 0 4px 14px rgba(0,0,0,0.12);
    overflow: hidden;
  }
  .identity {
    position: absolute;
    left: 44px;
    top: 26px;
  }
  .identity__accent {
    position: absolute;
    left: -12px;
    top: -4px;
    width: 36px;
    height: 38px;
  }
  .identity__name {
    position: relative;
    font-weight: 600;
    font-size: 44px;
    line-height: 1.0;
    color: var(--mint);
  }
  .identity__name .surname { font-weight: 500; display: block; }
  .identity__role {
    margin-top: 14px;
    font-weight: 500;
    font-size: 15px;
    letter-spacing: 5px;
    color: var(--accent-orange);
  }
  .contacts {
    position: absolute;
    left: 430px;
    top: 56px;
    font-weight: 300;
    font-size: 26px;
    line-height: 1.45;
    color: var(--contact-tan);
  }
  .brand {
    position: absolute;
    right: 48px;
    top: 50%;
    transform: translateY(-50%);
    display: flex;
    align-items: center;
    gap: 14px;
  }
  .brand__dot {
    width: 30px;
    height: 30px;
    border-radius: 50%;
    background: var(--accent-orange);
  }
  .brand__name {
    font-weight: 500;
    font-size: 30px;
    line-height: 1;
    color: var(--white);
  }
</style>
</head>
<body>
  <main class="canvas">
    <section class="signature" aria-label="Assinatura de e-mail">
      <div class="identity">
        <svg class="identity__accent" viewBox="0 0 36 38" aria-hidden="true">
          <polygon points="0,0 36,0 0,38" fill="var(--accent-orange)"/>
        </svg>
        <h1 class="identity__name">Marina <span class="surname">Tavares</span></h1>
        <p class="identity__role">GERENTE</p>
      </div>

      <div class="contacts">
        <p class="contacts__phone">(00) 98000-3156</p>
        <p class="contacts__social">@tidynestcleaning</p>
      </div>

      <div class="brand">
        <span class="brand__dot" aria-hidden="true"></span>
        <span class="brand__name">TidyNest</span>
      </div>
    </section>
  </main>
</body>
</html>
```